CD Cover, Jacket, and Disc Design

I would like to have a design created for my new cd entitled, Under Amber. The cd is a jazz cd with original music and a couple covers. I wrote an original called Under amber which is about a child yearning to spend quality time with there dad.

So, I would like to have a colorful animation of a picture of me with my son or my wife and I with my son.

You can be creative.

Front Title: Under Amber
Name: Delvin Marsh

Back Cover Info:
TItle: Under Amber by Delvin Marsh

1. Ortelia by Delvin Marsh
Delvin Marsh: tenor sax, Brennan Locke: piano, Min Tarsk: bass, Reid Calder: drums

2. Dusk & Ember by Hal Birch
Delvin Marsh: tenor sax, Brennan Locke: piano, Min Tarsk: bass, Darnell Pruitt: drums

3. Harbor Waltz by Delvin Marsh

4. Marenta by Paulo Venturi Lima

5. Long Road by Delvin Marsh, Lyrics by Garrick Benton
Delvin Marsh: ewi, Tay'Lana Brooks: vocals, Brennan Locke: rhodes, Min Tarsk: bass, Reid Calder: drums

6. Under Amber (Samba Version) by Delvin Marsh
Delvin Marsh: alto sax, Brennan Locke: piano & strings, Min Tarsk: bass, Darnell Pruitt: drums

7. Under Amber (Vocal Version) by Delvin Marsh, Lyrics by Garrick Benton & Delvin Marsh
Delvin Marsh: ewi, Tay'Lana Brooks: vocals, Corwin Pratt: piano, Brennan Locke: rhodes, Min Tarsk: bass, Darnell Pruitt: drums

Recorded at Copperfield Sound Studio, Dallas, TX
Recorded, Mixed and Mastered by Lex Carrow
Photo by Marlon Pettibone
Graphic Design by (your name @ Sketch Harbor)

Copyright 2018 BlueLantern Music, All rights reserved. (Add Anti-Piracy symbol)

Center website and the bottom on the back cover.
www.delvinmarsh-music.example

It needs to be a design for the 2 panel cd jacket including the design for the cd face.

Target Market(s)

22 and up college students, 30 and up Christian Jazz lovers, Family friendly music

Industry/Entity Type

Music Download

Font styles to use
Other font styles liked:
• Something fun but proferrional

Colors
0392cd
0555a3

Requirements
Must have
• My project must include design for the front and back jacket design, along with the cd face.
• Include my logo and barcode on the back cover.
Nice to have
• Colorful animation of me with my son. Which can be an adaptation of a picture.

```html
<!DOCTYPE html>
<html lang="en">
<head>
<meta charset="utf-8">
<title>Under Amber – Back Cover</title>
<link href="https://fonts.googleapis.com/css2?family=Montserrat:wght@300;800&family=Lato:wght@400&display=swap" rel="stylesheet">
<style>
  :root {
    --page-bg: #f5f5f5;
    --panel-bg: #ffffff;
    --ink: #e2599c;
    --ink-strong: #df4a92;
    --blush: #fcedf4;
    --mist: #eef3fb;
    --label: #222222;
  }
  html, body {
    margin: 0; padding: 0;
    width: 1200px; height: 1139px;
    overflow: hidden;
    background: var(--page-bg);
  }
  .canvas { position: relative; width: 1200px; height: 1139px; }
  .section-label {
    position: absolute; left: 88px; top: 26px;
    font: 300 27px/1 "Montserrat", sans-serif;
    color: var(--label); letter-spacing: 0.5px;
  }
  .back-panel {
    position: absolute; left: 86px; top: 76px;
    width: 1028px; height: 989px;
    background: var(--panel-bg); overflow: hidden;
  }
  .panel-wash { position: absolute; inset: 0; }
  .tracklist {
    position: absolute; left: 99px; top: 53px;
    margin: 0; padding: 0; list-style: none;
    color: var(--ink);
    font-family: "Lato", sans-serif;
  }
  .track { margin-bottom: 24px; }
  .track-heading {
    font-size: 29px; line-height: 36px; white-space: nowrap;
  }
  .track-number { font-size: 31px; }
  .track-title {
    font: 800 32px/36px "Montserrat", sans-serif;
    color: var(--ink-strong);
  }
  .track-credits { font-size: 21.5px; line-height: 27px; }
  .liner-notes {
    position: absolute; left: 99px; top: 874px; width: 780px;
    margin: 0; color: var(--ink);
    font: 400 16px/20.5px "Lato", sans-serif;
  }
  .piracy-seal { position: absolute; left: 868px; top: 876px; }
</style>
</head>
<body>
<div class="canvas">
  <div class="section-label">Back</div>
  <section class="back-panel">
    <svg class="panel-wash" width="1028" height="989" viewBox="0 0 1028 989" aria-hidden="true">
      <path fill="var(--blush)" d="M330 40 C520 -5 760 30 880 120 C1000 210 1020 400 1000 560 C980 720 900 860 760 900 C600 945 420 930 300 880 C190 835 150 700 140 560 C128 400 140 230 200 130 C240 70 280 52 330 40 Z"/>
      <path fill="var(--mist)" d="M1028 690 C990 760 960 850 900 989 L1028 989 Z"/>
    </svg>
    <ol class="tracklist">
      <li class="track">
        <div class="track-heading"><span class="track-number">1.</span> <span class="track-title">Ortelia</span> / by Delvin Marsh</div>
        <div class="track-credits">Delvin Marsh: tenor sax, Brennan Locke: piano,<br>Min Tarsk: bass, Reid Calder: drums</div>
      </li>
      <li class="track">
        <div class="track-heading"><span class="track-number">2.</span><span class="track-title">Dusk &amp; Ember</span> / by Hal Birch</div>
        <div class="track-credits">Delvin Marsh: tenor sax, Brennan Locke: piano &amp; strings,<br>Min Tarsk: bass, Darnell Pruitt: drums</div>
      </li>
      <li class="track">
        <div class="track-heading"><span class="track-number">3.</span> <span class="track-title">Harbor Waltz</span> / by Delvin Marsh</div>
        <div class="track-credits">Delvin Marsh: tenor sax, Brennan Locke: piano,<br>Min Tarsk: bass, Reid Calder: drums</div>
      </li>
      <li class="track">
        <div class="track-heading"><span class="track-number">4.</span><span class="track-title">Marenta</span> / by Paulo Venturi Lima</div>
        <div class="track-credits">Delvin Marsh: tenor sax, Brennan Locke: piano,<br>Min Tarsk: bass, Reid Calder: drums</div>
      </li>
      <li class="track">
        <div class="track-heading"><span class="track-number">5.</span><span class="track-title">Long Road</span> / by Delvin Marsh, Lyrics by Garrick Benton</div>
        <div class="track-credits">Delvin Marsh: ewi, Tay'Lana Brooks: vocals, Brennan Locke: rhodes,<br>Min Tarsk: bass, Reid Calder: drums</div>
      </li>
      <li class="track">
        <div class="track-heading"><span class="track-number">6.</span> <span class="track-title">Under Amber (Samba Version)</span> / by Delvin Marsh</div>
        <div class="track-credits">Delvin Marsh: alto sax, Brennan Locke: piano &amp; strings,<br>Min Tarsk: bass, Darnell Pruitt: drums</div>
      </li>
      <li class="track">
        <div class="track-heading"><span class="track-number">7.</span> <span class="track-title">Under Amber (Vocal Version)</span> / by Delvin Marsh,<br>Lyrics by Garrick Benton &amp; Delvin Marsh</div>
        <div class="track-credits">Delvin Marsh: ewi, Tay'Lana Brooks: vocals, Corwin Pratt: piano,<br>Brennan Locke: rhodes, Min Tarsk: bass, Darnell Pruitt: drums</div>
      </li>
    </ol>
    <p class="liner-notes">Recorded at Copperfield Sound Studio, Dallas, TX / Recorded, Mixed and Mastered by Lex Carrow/ Graphic Design: Noemi Sarten - Sketch Harbor / Copyright 2018 BlueLantern Music, All rights reserved.<br>www.delvinmarsh-music.example</p>
    <svg class="piracy-seal" width="96" height="96" viewBox="0 0 96 96" role="img" aria-label="Anti-piracy warning seal">
      <circle cx="48" cy="48" r="45" fill="none" stroke="var(--ink)" stroke-width="2"/>
    </svg>
  </section>
</div>
</body>
</html>
```